Advertising brochure for Trail Along Southside

We need a new single sided DL flier for the 2020 season!<br/>This flier is for our tour business. You can find all the details about the tour at our web site http://trailalong.southside.example<br/>The flier needs to grab the tourists attention, explain the tour and give price. I will upload a copy of last year's flier for your reference.<br/>We'd like the flier to match our web site to some extent.<br/>The most up to date information is on the web site and NOT last year's brochure. Use the web site for tour itinerary. We NO LONGER do the "Orchard Walk".<br/>Remember the size is "DL". Please no A4 format etc.<br/>You will be able to source images from:<br/>- Our web site<br/>- Our Chatterbook<br/>- Roamreview<br/>- Quarrel Listings<br/>If you have a particular idea in mind then feel free to contact us and we will try to accommodate your photo request.<br/>Good luck!

Target Market(s)

All ages

Industry/Entity Type

Tourism

Requirements
Must have
• Phone number
• Web Site
• Email address
• Price
Nice to have
• Description of tour and images

```html
<!DOCTYPE html>
<html lang="en">
<head>
<meta charset="utf-8">
<title>Trail Along Southside – The Tour DL Flier</title>
<link rel="stylesheet" href="https://fonts.googleapis.com/css2?family=Montserrat:wght@400;500;600;700;800&display=swap">
<style>
  :root {
    --orange: #f7821b;
    --orange-deep: #ee6f0a;
    --grey-title: #8c8c8c;
    --grey-band: #9d9d9d;
    --ink: #222222;
    --paper: #ffffff;
    --backdrop: #efefef;
  }
  * { margin: 0; padding: 0; box-sizing: border-box; }
  html, body { width: 1200px; height: 2278px; overflow: hidden; background: var(--backdrop); }
  body { font-family: "Montserrat", Arial, sans-serif; position: relative; }

  .flier {
    position: absolute; left: 150px; top: 193px;
    width: 900px; height: 1892px;
    background: var(--paper);
    box-shadow: 0 6px 24px rgba(0,0,0,.12);
    overflow: hidden;
  }
  .flier-art { position: absolute; inset: 0; }

  .flier-copy { position: absolute; left: 0; right: 0; text-align: center; }
  .tour-title {
    top: 975px; font-size: 84px; font-weight: 800; color: var(--grey-title);
    letter-spacing: 1px; line-height: 1;
  }
  .title-rule {
    position: absolute; top: 1102px; left: 347px; width: 207px; height: 5px; background: var(--orange);
  }
  .tour-summary {
    top: 1148px; font-size: 22.5px; font-weight: 500; color: var(--ink); line-height: 28px; padding: 0 70px;
  }
  .tour-price {
    top: 1312px; font-size: 60px; font-weight: 800; color: var(--orange); line-height: 1;
  }
  .price-note {
    top: 1394px; font-size: 22px; font-weight: 500; color: var(--ink); text-transform: uppercase;
  }
  .call-line {
    top: 1449px; font-size: 46px; font-weight: 500; color: var(--orange); line-height: 1;
  }
  .call-line .phone { font-weight: 700; color: var(--ink); }

  .brand-badge {
    position: absolute; left: 332px; top: 1527px; width: 236px; height: 236px;
    border-radius: 50%; background: var(--orange);
    display: flex; align-items: center; justify-content: center; text-align: center;
    color: var(--paper); font-size: 27px; font-weight: 600; line-height: 1.2; padding: 0 30px;
  }

  .contact-bar {
    position: absolute; left: 0; right: 0; top: 1832px;
    display: flex; justify-content: space-around; padding: 0 30px;
    color: var(--paper); font-size: 22px; font-weight: 600;
  }
  .contact-item { display: flex; align-items: center; gap: 12px; }
  .contact-item svg { width: 24px; height: 24px; flex: none; }
</style>
</head>
<body>
  <article class="flier">
    <svg class="flier-art" viewBox="0 0 900 1892" width="900" height="1892" xmlns="http://www.w3.org/2000/svg">
      <defs>
        <linearGradient id="heroTones" x1="0" y1="0" x2="0" y2="1">
          <stop offset="0" stop-color="#b9c4cb"/>
          <stop offset=".5" stop-color="#c7bdb3"/>
          <stop offset=".72" stop-color="#9a6a4a"/>
          <stop offset="1" stop-color="#7d5a3f"/>
        </linearGradient>
        <linearGradient id="convoyTones" x1="0" y1="0" x2="1" y2="1">
          <stop offset="0" stop-color="#cbbfa8"/>
          <stop offset="1" stop-color="#a99a82"/>
        </linearGradient>
        <linearGradient id="fieldTones" x1="0" y1="0" x2="0" y2="1">
          <stop offset="0" stop-color="#dbe4e6"/>
          <stop offset=".5" stop-color="#d9b48e"/>
          <stop offset="1" stop-color="#b97a4a"/>
        </linearGradient>
        <linearGradient id="mineTones" x1="0" y1="0" x2="1" y2="1">
          <stop offset="0" stop-color="#6f5a4a"/>
          <stop offset="1" stop-color="#3f3a36"/>
        </linearGradient>
      </defs>

      <g role="img" aria-label="Photo of a rusty vintage mining truck with a drill rig among pale spoil heaps under a grey sky">
        <rect x="0" y="0" width="900" height="640" fill="url(#heroTones)"/>
      </g>
      <path d="M0 470 Q450 720 900 470 L900 1892 L0 1892 Z" fill="var(--paper)"/>
      <path d="M0 505 Q450 735 900 505" fill="none" stroke="var(--grey-band)" stroke-width="14"/>
      <path d="M0 470 Q450 720 900 470 L900 520 Q450 760 0 520 Z" fill="var(--paper)"/>

      <g role="img" aria-label="Photo of the desert opal fields stretching to the horizon">
        <circle cx="450" cy="605" r="183" fill="url(#fieldTones)"/>
      </g>
      <g role="img" aria-label="Aerial photo of a convoy of cars driving along a dusty desert track">
        <circle cx="225" cy="725" r="174" fill="url(#convoyTones)" stroke="var(--orange)" stroke-width="4"/>
      </g>
      <g role="img" aria-label="Photo of visitors in hard hats exploring machinery inside an underground mine">
        <circle cx="675" cy="725" r="174" fill="url(#mineTones)" stroke="var(--orange)" stroke-width="4"/>
      </g>

      <path d="M0 1688 L290 1688 Q330 1688 355 1712 Q390 1745 450 1745 Q510 1745 545 1712 Q570 1688 610 1688 L900 1688"
            fill="none" stroke="var(--orange)" stroke-width="7"/>
      <path d="M0 1705 L290 1705 Q330 1705 355 1729 Q390 1762 450 1762 Q510 1762 545 1729 Q570 1705 610 1705 L900 1705 L900 1892 L0 1892 Z"
            fill="var(--grey-band)"/>
    </svg>

    <h1 class="flier-copy tour-title">THE TOUR</h1>
    <div class="title-rule"></div>
    <p class="flier-copy tour-summary">
      A Unique Tag-along Journey Through Ochre Flats.<br>
      Enjoy A Tour From The Comfort Of Your Own Car As Our<br>
      Experienced Guide Takes You Through A "Day In The Life" Of A<br>
      Ochre Flats Miner.<br>
      Scroll Down To See What You're In For.
    </p>
    <p class="flier-copy tour-price">$40 PER PERSON</p>
    <p class="flier-copy price-note">(Kids half price and children under 5 free!)</p>
    <p class="flier-copy call-line">CALL US NOW: <span class="phone">61 8 5550 0148</span></p>

    <div class="brand-badge">Trail Along Southside</div>

    <div class="contact-bar">
      <span class="contact-item">
        <svg viewBox="0 0 24 24" fill="none" stroke="#ffffff" stroke-width="2"><circle cx="12" cy="12" r="10"/><path d="M2 12h20M12 2c3 3 4.5 6.5 4.5 10S15 19 12 22c-3-3-4.5-6.5-4.5-10S9 5 12 2z"/></svg>
        trailalong.southside.example
      </span>
      <span class="contact-item">
        <svg viewBox="0 0 24 24" fill="none" stroke="#ffffff" stroke-width="2"><rect x="2" y="5" width="20" height="14" rx="1"/><path d="M2 6l10 7 10-7"/></svg>
        hello@trailalong.southside.example
      </span>
    </div>
  </article>
</body>
</html>
```